Infografik für Tanzschule
Zielgruppe
Wir sind eine Tanzschule für die Tänze Salsa, Bachata, kizomba & Zouk in Freiburg
Aufgabenstellung
DESIGN-BRIEFING
Tarifübersicht – Tanzschule Ritmo del Alba
Projektziel
Gestaltung einer klaren, hochwertigen Tarifübersicht für eine Tanzschule.
Die Grafik dient: als Information & Orientierung auf der Homepage, als visuelle Grundlage für das Anmeldeformular vor Ort, Der Einstieg erfolgt immer über eine gratis Schnupperstunde.
Die verbindliche Anmeldung erfolgt nach der Schnupperstunde vor Ort über ein Formular mit Auswahlkästchen.
Grundaufbau
3 Tarifkarten nebeneinander
Einheitlicher, moderner Stil
evtl. Emotionale Bilder (echte Tanzszenen, echte Menschen)
Klare Hierarchie:
Titel → Preis → Erklärung → Vorteile → Auswahlkästchen
Struktur der Tarifkarten
KARTE 1 – EINSTIEG
Titel: 1× PRO WOCHE TANZEN
Preis: 56 €/ 39 € erm.
Subline: pro Person · pro Kalendermonat
Vorteile (max. 4 Bulletpoints):
Ein fester wöchentlicher Kurs
Klare Routine & Struktur
Ausweichstunde im selben Monat möglich (muss klar enthalten sein)
Auswahl: ☐ 1× pro Woche tanzen
KARTE 2 – REGELMÄSSIG TANZEN (darf visuell leicht hervorgehoben sein, z. B. Rahmen oder Badge)
Optionales Badge:
SEHR BELIEBT
Titel: 2× PRO WOCHE TANZEN
Preis: 98 € / 68 € erm.
Vorteile:
Zwei feste wöchentliche Kurse
Mehr Praxis & schnellerer Fortschritt
Ausweichstunde im selben Monat möglich
Auswahl:
☐ 2× pro Woche tanzen
KARTE 3 – MAXIMALE FREIHEIT
Titel: FLAT – ALL YOU CAN DANCE
Preis: ab 129 € / 99 € erm.
Alle Tänze
Alle Kurse (für dein Tanz-Level)
Alle Workshops (für dein Tanz-Level)
Maximale Freiheit
☐ FLAT 1 Monat – 149 € | 119 € erm. (monatlich kündbar)
☐ FLAT 3 Monate – 129 € | 99 € erm. (3 Monate Erstlaufzeit)
Einheitlicher Hinweis unter den Karten (kleiner Text)
Ausweic..

```html
<!DOCTYPE html>
<html lang="de">
<head>
<meta charset="utf-8">
<title>Anmeldeformular – Ritmo del Alba</title>
<link href="https://fonts.googleapis.com/css2?family=Inter:wght@300;400;500;600;700&family=Barlow+Condensed:wght@400;500;600;700&display=swap" rel="stylesheet">
<style>
:root{
  --backdrop:#9e9e9e;
  --paper:#ffffff;
  --ink:#222222;
  --muted:#5a5a5a;
  --line:#555555;
  --card:#f3f3f3;
  --card-head:#e6e6e6;
  --card-head-strong:#d9d9d9;
  --card-border:#d6d6d6;
  --accent:#2b2b2b;
  --bar:#cfcfcf;
  --band:#d8e2dd;
  --photo-a:#6f7c6a;
  --photo-b:#a69a88;
  --photo-c:#4c5a48;
}
*{box-sizing:border-box;margin:0;padding:0}
html,body{width:1200px;height:1200px;overflow:hidden;background:var(--backdrop)}
body{font-family:'Inter',sans-serif;color:var(--ink);position:relative}
.sheet{position:absolute;left:302px;top:179px;width:595px;height:841px;background:var(--paper);overflow:hidden}
.abs{position:absolute}
.hero{left:0;top:0;width:595px;height:268px;background:linear-gradient(180deg,#8d96a0 0%,var(--photo-b) 30%,var(--photo-a) 60%,var(--photo-c) 100%)}
.hero-title{left:31px;top:16px;font-size:17px;font-weight:700;color:#fff;letter-spacing:-.4px}
.brand{left:446px;top:86px;font-size:11px;font-weight:400;color:#fff;display:flex;align-items:center;gap:5px}
.brand-dot{width:7px;height:7px;border-radius:50%;background:#fff}
.form-panel{left:23px;top:127px;width:550px;height:160px;background:var(--paper);border-radius:7px}
.form-label{font-size:9px;color:var(--ink);left:42px}
.form-colon{left:137px;font-size:9px}
.form-line{left:143px;width:267px;border-bottom:.8px solid var(--line)}
.box{display:inline-block;flex:none;width:7px;height:7px;border:.8px solid var(--ink);border-radius:1.5px;vertical-align:-1px}
.salutation{left:42px;top:141px;font-size:8px;display:flex;gap:4px;align-items:center}
.opt{font-size:9px;left:42px;display:flex;gap:7px;align-items:center}
.contact{left:427px;top:136px;width:128px;height:146px;background:#f1f1f1;border:.8px solid #dcdcdc;border-radius:6px;padding:10px 5px;font-size:7.7px;line-height:11px;color:#333}
.contact b{font-weight:600;color:var(--ink)}
.contact p{margin-bottom:15px}
.contact p:last-child{margin:0;margin-top:-2px;line-height:14px}
.card{top:308px;width:173px;height:265px;background:var(--card);border:.8px solid var(--card-border);border-radius:6px;overflow:hidden}
.card.featured{border:1px solid var(--accent)}
.card-head{height:104px;background:var(--card-head);position:relative;padding:12px 0 0 22px}
.featured .card-head{background:var(--card-head-strong)}
.card-bar{position:absolute;left:10px;top:12px;width:4px;height:82px;background:var(--bar)}
.featured .card-bar{background:var(--accent)}
.card-title{font-size:17px;font-weight:300;line-height:17px;color:var(--ink);letter-spacing:-.3px}
.price{font-family:'Barlow Condensed',sans-serif;display:flex;align-items:flex-start;margin-top:5px;height:30px}
.price .cur{font-size:9px;font-weight:600;margin-top:2px}
.price .num{font-size:29px;font-weight:600;line-height:29px;letter-spacing:-.5px}
.price .red{font-size:9px;font-weight:600;margin-top:14px;margin-left:4px}
.featured .price .red{margin-top:9px}
.per{font-family:'Barlow Condensed',sans-serif;font-size:9.5px;color:var(--muted);margin-top:3px}
.card-body{padding:10px 10px 0 10px}
.perks-title{font-size:9px;font-weight:600;margin-bottom:3px}
.perks{list-style:none;font-size:8.5px;color:#444;line-height:12px}
.perks li{display:flex;gap:5px;margin-bottom:2px}
.perks svg{flex:none;margin-top:2px}
.choices{position:absolute;left:10px;right:8px;top:200px;border-top:.8px solid var(--card-border);padding-top:6px;font-size:8px;font-weight:600;letter-spacing:-.15px}
.choice{display:flex;gap:6px;align-items:center;white-space:nowrap;line-height:12px}
.choice-note{font-size:7.5px;font-style:italic;font-weight:400;color:#555;line-height:10px;margin:1px 0 5px;letter-spacing:0}
.badge{left:249px;top:301px;width:70px;height:14px;border-radius:7px;background:var(--accent);color:#fff;font-size:8.5px;font-weight:600;text-align:center;line-height:14px}
.note-title{font-size:9px;font-weight:600;top:595px}
.note-text{top:609px;font-size:8.5px;font-style:italic;color:#555;line-height:12.5px;border-left:2px solid #cfcfcf;padding-left:8px}
.band{left:0;top:655px;width:595px;height:186px;background:var(--band)}
.sepa{left:47px;top:668px;width:532px;height:103px;background:#fff;padding:5px 9px 0 9px;font-family:'Barlow Condensed',sans-serif}
.sepa-title{font-size:8px;font-weight:600;line-height:10px}
.sepa-text{font-size:6.7px;line-height:9px;color:#444}
.bank{position:absolute;left:9px;top:46px;width:516px;height:49px;border:1px solid #333;font-size:6.8px}
.bank .row1{height:24px;border-bottom:1px solid #333;display:flex}
.bank .cell{padding:2px 5px}
.bank .cell:first-child{width:296px;border-right:1px solid #333}
.iban{position:absolute;left:5px;top:28px}
.months{left:47px;top:783px;width:214px;height:26px;background:#fff;display:flex;justify-content:space-around;padding:5px 6px 0;font-family:'Barlow Condensed',sans-serif;font-size:6.5px;font-weight:500}
.month{display:flex;flex-direction:column;align-items:center;gap:1px}
.sign{left:330px;top:783px;width:249px;height:32px;background:#fff}
.foot{font-family:'Barlow Condensed',sans-serif;font-size:12.5px;font-weight:500;color:var(--ink)}
.foot small{font-size:6.5px;font-weight:600;margin-left:3px}
</style>
</head>
<body>
<main class="sheet">
  <div class="abs hero" role="img" aria-label="Gruppenfoto des Tanzschul-Teams vor der Stadtkulisse von Freiburg"></div>
  <h1 class="abs hero-title">Anmeldeformular</h1>
  <div class="abs brand"><span class="brand-dot"></span>Ritmo del Alba</div>

  <div class="abs form-panel"></div>
  <div class="abs salutation">Frau <span class="box"></span> Herr <span class="box"></span> Div. <span class="box"></span></div>
  <span class="abs form-label" style="top:158px">Vorname / Nachname :</span>
  <span class="abs form-label" style="top:178px">Straße / Nr</span><span class="abs form-colon" style="top:178px">:</span>
  <span class="abs form-label" style="top:198px">PLZ/Ort</span><span class="abs form-colon" style="top:198px">:</span>
  <span class="abs form-label" style="top:218px">Telefon</span><span class="abs form-colon" style="top:218px">:</span>
  <span class="abs form-label" style="top:238px">E-mail</span><span class="abs form-colon" style="top:238px">:</span>
  <div class="abs form-line" style="top:169px"></div>
  <div class="abs form-line" style="top:189px"></div>
  <div class="abs form-line" style="top:209px"></div>
  <div class="abs form-line" style="top:229px"></div>
  <div class="abs form-line" style="top:249px"></div>
  <div class="abs opt" style="top:258px"><span class="box"></span>Ermäßigt (Student*in / Schüler*in / Auszubildende*r)</div>
  <div class="abs opt" style="top:274px"><span class="box"></span>Ja, ich möchte den Newsletter und Kursinformationen erhalten.</div>

  <aside class="abs contact">
    <p><b>Tanzschule Ritmo del Alba</b><br>Lindenweg 14 79098 Freiburg</p>
    <p><b>Geschäftsanschrift</b><br>Ritmo del Alba Lukas Brenner<br>Uferstr. 8 79104 Freiburg</p>
    <p><b>T&nbsp;&nbsp;:</b> +49 152 000 418 60<br><b>M :</b> info@ritmo-del-alba.de<br><b>W :</b> www.ritmo-del-alba.de</p>
  </aside>

  <svg width="0" height="0" style="position:absolute">
    <symbol id="tick" viewBox="0 0 8 8"><rect x=".5" y=".5" width="7" height="7" rx="1.2" fill="none" stroke="#555" stroke-width=".8"/><path d="M2 4.2l1.5 1.5L6.3 2.4" fill="none" stroke="#555" stroke-width=".9"/></symbol>
  </svg>

  <section class="abs card" style="left:31px">
    <div class="card-head"><span class="card-bar"></span>
      <div class="card-title">1× Pro Woche<br>Tanzen</div>
      <div class="price"><span class="cur">€</span><span class="num">56</span><span class="red">/ 39 € erm.</span></div>
      <div class="per">pro Person / Kalendermonat</div>
    </div>
    <div class="card-body">
      <div class="perks-title">Vorteile</div>
      <ul class="perks">
        <li><svg width="7" height="7"><use href="#tick"/></svg>Ein fester wöchentlicher Kurs</li>
        <li><svg width="7" height="7"><use href="#tick"/></svg>Klare Routine &amp; Struktur</li>
        <li><svg width="7" height="7"><use href="#tick"/></svg>Ausweichstunde im selben Monat möglich</li>
      </ul>
    </div>
    <div class="choices"><div class="choice"><span class="box"></span>1× pro Woche tanzen</div></div>
  </section>

  <section class="abs card featured" style="left:211px">
    <div class="card-head"><span class="card-bar"></span>
      <div class="card-title">Regelmässig<br>Tanzen</div>
      <div class="price"><span class="cur">€</span><span class="num">98</span><span class="red">/ 68 € erm.</span></div>
      <div class="per">pro Person / Kalendermonat</div>
    </div>
    <div class="card-body">
      <div class="perks-title">Vorteile</div>
      <ul class="perks">
        <li><svg width="7" height="7"><use href="#tick"/></svg>Zwei feste wöchentliche Kurse</li>
        <li><svg width="7" height="7"><use href="#tick"/></svg>Mehr Praxis &amp; schnellerer Fortschritt</li>
        <li><svg width="7" height="7"><use href="#tick"/></svg>Ausweichstunde im selben Monat möglich</li>
      </ul>
    </div>
    <div class="choices"><div class="choice"><span class="box"></span>2× pro Woche tanzen</div></div>
  </section>
  <div class="abs badge">Sehr Beliebt</div>

  <section class="abs card" style="left:390px">
    <div class="card-head"><span class="card-bar"></span>
      <div class="card-title">Flat – All You Can<br>Dance</div>
      <div class="price"><span class="cur" style="font-size:10px;margin-top:1px">ab</span><span class="num">129</span><span class="cur">€</span><span class="red">/ 99 € erm.</span></div>
      <div class="per">pro Person / Kalendermonat</div>
    </div>
    <div class="card-body">
      <div class="perks-title">Vorteile</div>
      <ul class="perks">
        <li><svg width="7" height="7"><use href="#tick"/></svg>Alle Tänze</li>
        <li><svg width="7" height="7"><use href="#tick"/></svg>Alle Kurse (für dein Tanz-Level)</li>
        <li><svg width="7" height="7"><use href="#tick"/></svg>Alle Workshops (für dein Tanz-Level)</li>
        <li><svg width="7" height="7"><use href="#tick"/></svg>Maximale Freiheit</li>
      </ul>
    </div>
    <div class="choices">
      <div class="choice"><span class="box"></span>FLAT 1 Monat – 149 € | 119 € erm.</div>
      <div class="choice-note">(monatlich kündbar)</div>
      <div class="choice"><span class="box"></span>FLAT 3 Monate – 129 € | 99 € erm.</div>
      <div class="choice-note">(3 Monate Erstlaufzeit)</div>
    </div>
  </section>

  <h3 class="abs note-title" style="left:47px">Hinweis</h3>
  <p class="abs note-text" style="left:47px;width:150px">Ausweichstunde: Im selben Kalendermonat möglich.</p>
  <h3 class="abs note-title" style="left:226px">Verlängerung &amp; Kündigung</h3>
  <p class="abs note-text" style="left:226px;width:352px">Der Vertrag verlängert sich automatisch um jeweils einen Monat und ist mit 14 Tagen Frist zum Monatsende kündbar.<br>Ausnahme: FLAT 3 Monate – kündbar nach Ablauf der Erstlaufzeit.</p>

  <div class="abs band"></div>
  <section class="abs sepa">
    <div class="sepa-title">Einzugsermächtigung / SEPA-Lastschriftmandat</div>
    <p class="sepa-text">Ich ermächtige Ritmo del Alba, Zahlungen von meinem Konto per Lastschrift einzuziehen und mein Kreditinstitut, diese Lastschriften einzulösen. Bei Ablehnung der Lastschrift fallen Kosten von 10,00 € pro Rückbuchung an. Ich kann innerhalb von acht Wochen ab Belastungsdatum die Erstattung verlangen, gemäß den Bedingungen meines Kreditinstituts. Die Kursgebühr wird im ersten Monat zur Mitte/Ende eingezogen, danach jeweils am 05. jedes Monats.</p>
    <div class="bank">
      <div class="row1"><div class="cell">Kreditinstitut:</div><div class="cell">BIC: - Beginnt die IBAN mit DE, dann ist kein BIC nötig</div></div>
      <span class="iban">IBAN:</span>
      <svg class="abs" style="left:0;top:24px" width="516" height="24" viewBox="0 0 516 24">
        <g stroke="#333" stroke-width=".8">
          <line x1="27" y1="12" x2="27" y2="22"/><line x1="48" y1="14" x2="48" y2="22"/><line x1="68" y1="14" x2="68" y2="22"/><line x1="89" y1="14" x2="89" y2="22"/>
          <line x1="110" y1="8" x2="110" y2="22"/><line x1="130" y1="14" x2="130" y2="22"/><line x1="151" y1="14" x2="151" y2="22"/><line x1="172" y1="14" x2="172" y2="22"/>
          <line x1="192" y1="8" x2="192" y2="22"/><line x1="213" y1="14" x2="213" y2="22"/><line x1="234" y1="14" x2="234" y2="22"/><line x1="254" y1="14" x2="254" y2="22"/>
          <line x1="275" y1="8" x2="275" y2="22"/><line x1="296" y1="14" x2="296" y2="22"/><line x1="316" y1="14" x2="316" y2="22"/><line x1="337" y1="14" x2="337" y2="22"/>
          <line x1="358" y1="8" x2="358" y2="22"/><line x1="378" y1="14" x2="378" y2="22"/><line x1="399" y1="14" x2="399" y2="22"/><line x1="420" y1="14" x2="420" y2="22"/>
          <line x1="440" y1="8" x2="440" y2="22"/><line x1="461" y1="14" x2="461" y2="22"/><line x1="482" y1="14" x2="482" y2="22"/>
        </g>
        <text x="33" y="20" font-family="Barlow Condensed, sans-serif" font-size="13" font-weight="500" fill="#222">D</text>
        <text x="54" y="20" font-family="Barlow Condensed, sans-serif" font-size="13" font-weight="500" fill="#222">E</text>
      </svg>
    </div>
  </section>

  <div class="abs months">
    <div class="month">Jan<span class="box"></span></div><div class="month">Feb<span class="box"></span></div><div class="month">Mrz<span class="box"></span></div><div class="month">Apr<span class="box"></span></div><div class="month">Mai<span class="box"></span></div><div class="month">Jun<span class="box"></span></div><div class="month">Jul<span class="box"></span></div><div class="month">Aug<span class="box"></span></div><div class="month">Sep<span class="box"></span></div><div class="month">Okt<span class="box"></span></div><div class="month">Nov<span class="box"></span></div><div class="month">Dez<span class="box"></span></div>
  </div>
  <div class="abs foot" style="left:48px;top:812px">Kursstart / Anmeldung ab:</div>
  <div class="abs sign"></div>
  <div class="abs foot" style="left:330px;top:819px">Datum / Unterschrift: <small>Wir verweisen auf unsere umseitig abgedruckten AGB</small></div>
</main>
</body>
</html>
```